Flooring & Interior Design showroom

Just bought this business- Kestrel Lane Flooring & Interiors. Love our logo (we are on Kestrel Lane )and colors
Forest green, gold and black
Love that the back lists everything we do. We no longer have plenotilex but need to add in LVP/ SPC and need to take out vantor shadehub logo at the bottom and use the quib logo instead (maybe? open to suggestions)

Not in love with our cards- I want a higher end look
I hate the gradient poop color we have now.
Would love if they were all black - maybe or ??
or had a foil or embossing?

```html
<!DOCTYPE html>
<html lang="en">
<head>
<meta charset="utf-8">
<title>Kestrel Lane Flooring &amp; Interiors — Business Cards</title>
<link rel="stylesheet" href="https://fonts.googleapis.com/css2?family=Cinzel:wght@600&family=Arimo:wght@400&display=swap">
<style>
  :root {
    --stage: #2a2a2a;
    --card-black: #050505;
    --forest: #3b6b46;
    --sage-text: #a3d3a0;
    --leaf-text: #7fb98a;
    --gold: #dcc78c;
    --gold-soft: #e9dba8;
    --divider: #6c6c6c;
  }
  * { margin: 0; padding: 0; box-sizing: border-box; }
  html, body { width: 1200px; height: 900px; overflow: hidden; }
  body {
    background: var(--stage);
    font-family: "Arimo", Arial, sans-serif;
    position: relative;
  }
  .card {
    position: absolute;
    left: 285px;
    width: 630px;
    height: 360px;
    background: var(--card-black);
    overflow: hidden;
  }
  .card--back { top: 60px; }
  .card--front { top: 480px; }

  .band {
    position: absolute;
    left: 0; right: 0; bottom: 0;
    background: var(--forest);
    display: flex;
    align-items: center;
  }
  .card--front .band { height: 78px; justify-content: center; padding-left: 150px; }
  .card--back .band { height: 48px; justify-content: space-between; padding: 0 34px; }
  .band-text { color: var(--gold-soft); font-size: 17px; }
  .card--back .band-text { font-size: 15px; }

  /* business name set as plain text */
  .brand-name {
    position: absolute;
    font-family: "Arimo", Arial, sans-serif;
    font-weight: 400;
    color: var(--gold);
    line-height: 1.2;
  }
  .brand-name .brand-main { display: block; font-size: 30px; }
  .brand-name .brand-sub { display: block; font-size: 16px; margin-top: 4px; }
  .card--front .brand-name { left: 36px; top: 168px; }
  .card--back .brand-name { left: 34px; top: 36px; }

  /* front */
  .divider {
    position: absolute;
    left: 290px; top: 70px;
    width: 1px; height: 200px;
    background: var(--divider);
  }
  .contact { position: absolute; left: 312px; top: 40px; }
  .person-name {
    font-family: "Cinzel", serif;
    font-weight: 600;
    font-size: 27px;
    color: var(--gold);
    letter-spacing: 1px;
    line-height: 1;
  }
  .person-role { color: var(--leaf-text); font-size: 16px; margin-top: 4px; }
  .contact-lines { list-style: none; margin-top: 14px; }
  .contact-lines li { color: var(--gold-soft); font-size: 14.5px; line-height: 19px; }
  .address { margin-top: 12px; color: var(--leaf-text); font-size: 15px; line-height: 19px; }

  /* back */
  .partners {
    position: absolute;
    right: 34px; top: 34px;
    display: flex; align-items: center; gap: 26px;
  }
  .partner-name { color: var(--gold-soft); font-size: 15px; line-height: 1; }
  .review-name { display: flex; align-items: center; gap: 7px; color: var(--gold-soft); font-size: 15px; line-height: 1; }
  .review-mark { width: 10px; height: 10px; background: var(--gold); }

  .service-list { position: absolute; list-style: none; }
  .service-list li {
    color: var(--sage-text);
    font-size: 18px;
    line-height: 25px;
    padding-left: 16px;
    position: relative;
  }
  .service-list li::before {
    content: "";
    position: absolute;
    left: 2px; top: 10px;
    width: 6px; height: 6px;
    border-radius: 50%;
    background: var(--gold-soft);
  }
  .services--first { left: 40px; top: 140px; }
  .services--second { left: 230px; top: 112px; }
  .services--third { left: 462px; top: 100px; }
</style>
</head>
<body>

<section class="card card--back" aria-label="Card back: services">
  <div class="brand-name">
    <span class="brand-main">Kestrel Lane</span>
    <span class="brand-sub">Flooring &amp; Interiors</span>
  </div>

  <div class="partners">
    <span class="partner-name">Brindle Hale Window Fashions</span>
    <span class="review-name">Quib<span class="review-mark"></span></span>
  </div>

  <ul class="service-list services--first">
    <li>Area Rugs</li>
    <li>Bed Spreads</li>
    <li>Blinds</li>
    <li>Carpet</li>
    <li>Cork</li>
    <li>Fabric</li>
  </ul>
  <ul class="service-list services--second">
    <li>Hardwood</li>
    <li>Laminate</li>
    <li>LVP/ SPC</li>
    <li>Motorized Shades</li>
    <li>Pillows</li>
    <li>Sand &amp; refinish</li>
  </ul>
  <ul class="service-list services--third">
    <li>Sheers</li>
    <li>Shutters</li>
    <li>Upholstery</li>
    <li>Valances</li>
    <li>Verticals</li>
    <li>Vinyl</li>
  </ul>

  <div class="band">
    <span class="band-text">Home Town Service Since 1979</span>
    <span class="band-text">www.kestrellaneflooring.com</span>
  </div>
</section>

<section class="card card--front" aria-label="Card front: contact">
  <div class="brand-name">
    <span class="brand-main">Kestrel Lane</span>
    <span class="brand-sub">Flooring &amp; Interiors</span>
  </div>

  <div class="divider"></div>

  <div class="contact">
    <h1 class="person-name">OWEN MARLOW</h1>
    <p class="person-role">Salesperson</p>
    <ul class="contact-lines">
      <li>P: 555.204.3187</li>
      <li>M: 555.618.4092</li>
      <li>F: 555.377.9140</li>
      <li>E: owen@kestrellaneflooring.com</li>
      <li>W: www.kestrellaneflooring.com</li>
    </ul>
    <p class="address">214 Kestrel Lane<br>Harbor Point CA 90210</p>
  </div>

  <div class="band">
    <span class="band-text">CA Lic: 418273</span>
  </div>
</section>

</body>
</html>
```